Private practice for psychiatry and psychotherapy needs a business card and logo

I need a logo and business card design for my private practice for psychiatry and psychotherapy. The optional names for my practice are: Voskuilen Praktijk voor Psychiatrie en Psychotherapie, or short: Praktijk Voskuilen.
I am a (child and adolescent) psychiatrist and psychotherapist. I diagnose and treat infants, children, adolescents and adults with psychiatric symptoms/disorders. I also give supervision to colleagues about their own treatments. My work is characterised by personal involvement, transparence, creativity and professionality.
I would like to have an appealing, light and bright, yet basic design that invites people (both children and adults) to contact me, gives trust and hope, without loosing professional appearance.
I uploaded my contact information which should not necessarily be all included (in this form) on the card as long as people know how to contact me. Please feel free to be creative!
Please note that my website is only temporarely and need a new design and update too!

Target Market(s)

Clients and patients (children, adolescents, adults) with psychiatric symptoms who need diagnosis and treatment. I work with private clients and patients through medical insurances.

Industry/Entity Type

Mental Health

Contact Information for Business Card

Dr. Femke Voskuilen-ter Horst
Psychiater/Kinder- en Jeugdpsychiater
Gerrit Wassinkstraat 4
3063 TW Rotterdam
t: 06-58190274
e: info@praktijkvoskuilen-voorbeeld.nl
i: www.praktijkvoskuilen-voorbeeld.nl

Logo Text

Praktijk Voskuilen voor Psychiatrie en Psychotherapie; or short: Praktijk Voskuilen

Font styles to use
Sans Serif
Other font styles liked:
• up to designer

Requirements
Must have
• Appealing, light, bright, creative, trustful, professional and unique.

```html
<!DOCTYPE html>
<html lang="nl">
<head>
<meta charset="utf-8">
<title>Praktijk Voskuilen – Visitekaartje</title>
<link rel="stylesheet" href="https://fonts.googleapis.com/css2?family=Montserrat:wght@400;500;600&display=swap">
<style>
  :root {
    --bg: #ecebf1;
    --card: #ffffff;
    --wave-dark: #c9c9cc;
    --wave-light: #e2e2e4;
    --brand-blue: #2f3fa8;
    --text-grey: #8a8a8e;
    --text-dark: #6e6e72;
  }
  html, body {
    margin: 0;
    width: 1200px;
    height: 900px;
    overflow: hidden;
    background: var(--bg);
    font-family: "Montserrat", sans-serif;
  }
  .sheet {
    position: relative;
    width: 1200px;
    height: 900px;
  }
  .card {
    position: absolute;
    top: 282px;
    width: 520px;
    height: 336px;
    border-radius: 22px;
    background: var(--card);
    overflow: hidden;
    box-shadow: 0 10px 30px rgba(60, 60, 90, 0.15);
  }
  .card--front { left: 50px; }
  .card--back  { left: 630px; }
  .card__waves {
    position: absolute;
    inset: 0;
    width: 100%;
    height: 100%;
  }
  .wave--dark  { fill: var(--wave-dark); }
  .wave--light { fill: var(--wave-light); }

  .identity {
    position: absolute;
    left: 200px;
    right: 24px;
    top: 118px;
    text-align: center;
    color: var(--brand-blue);
  }
  .identity__mark {
    display: flex;
    align-items: center;
    justify-content: center;
    gap: 8px;
    font-size: 15px;
    font-weight: 600;
    margin-bottom: 14px;
  }
  .identity__dot {
    width: 12px;
    height: 12px;
    border-radius: 50%;
    background: var(--brand-blue);
  }
  .identity__name {
    font-size: 17px;
    font-weight: 600;
    letter-spacing: 0.02em;
    text-transform: uppercase;
    margin: 0;
  }
  .identity__role {
    font-size: 10px;
    font-weight: 500;
    margin: 6px 0 0;
    color: var(--brand-blue);
  }

  .contact {
    position: absolute;
    left: 32px;
    top: 38px;
    color: var(--text-grey);
  }
  .contact__name {
    font-size: 19px;
    font-weight: 500;
    margin: 0;
    color: var(--text-dark);
  }
  .contact__role {
    font-size: 12px;
    font-weight: 600;
    margin: 4px 0 18px;
    color: var(--text-dark);
  }
  .contact__address {
    font-size: 17px;
    line-height: 1.35;
    margin: 0 0 14px;
    font-style: normal;
  }
  .contact__lines {
    list-style: none;
    margin: 0;
    padding: 0;
    font-size: 11px;
    line-height: 1.7;
  }
</style>
</head>
<body>
<main class="sheet">

  <section class="card card--front" aria-label="Voorkant visitekaartje">
    <svg class="card__waves" viewBox="0 0 520 336" preserveAspectRatio="none" aria-hidden="true">
      <path class="wave--light" d="M0 0 H150 C90 70 230 150 200 230 C180 290 120 320 100 336 H0 Z"/>
      <path class="wave--dark" d="M0 0 H90 C40 80 170 150 140 230 C125 285 80 315 60 336 H0 Z"/>
    </svg>
    <div class="identity">
      <div class="identity__mark"><span class="identity__dot"></span>Praktijk Voskuilen</div>
      <p class="identity__name">Dr. Femke Voskuilen-ter Horst</p>
      <p class="identity__role">Psychiater/Kinder- en Jeugdpsychiater</p>
    </div>
  </section>

  <section class="card card--back" aria-label="Achterkant visitekaartje">
    <svg class="card__waves" viewBox="0 0 520 336" preserveAspectRatio="none" aria-hidden="true">
      <path class="wave--light" d="M520 0 H360 C420 70 290 150 330 230 C350 290 400 320 420 336 H520 Z"/>
      <path class="wave--dark" d="M520 0 H430 C480 80 360 150 390 230 C405 285 450 315 470 336 H520 Z"/>
    </svg>
    <div class="contact">
      <p class="contact__name">Dr. Femke Voskuilen-ter Horst</p>
      <p class="contact__role">Psychiater/Kinder- en Jeugdpsychiater</p>
      <address class="contact__address">Gerrit Wassinkstraat 4<br>3063 TW Rotterdam</address>
      <ul class="contact__lines">
        <li>t: 06-58190274</li>
        <li>e: info@praktijkvoskuilen-voorbeeld.nl</li>
        <li>i: www.praktijkvoskuilen-voorbeeld.nl</li>
      </ul>
    </div>
  </section>

</main>
</body>
</html>
```